Expanding National Maid Service Needs Redesign!

We need a redesigned home page for our residential cleaning company. Winner will be recognized as the designer for a brand about to go national within the United States. Winner will also become the first choice to continue working with the company to design at least 15 more pages.

Looking for redesign of homepage and redesign of logo (logo will use the same elements -- just organized differently with horizontal text).

For the design we are looking for a mix between the following websites:
www. brigadeofsweepers .com
This is our parent site that will be redesigned

www. tidycorsairs .com
We really like the top/header having the three steps.
We would like to have the same font (proxima nova) and colors. We like the location and size of the booking form.
Love the section topics and would like to mimic that.

www. brighthavenkeepers .com
We really like the clean art and use of colors.
We love the use of b-roll and branded images. Will provide for our website.

The perfect site would have the cleanliness, layout and booking form of Tidy Corsairs and the excellent placement and use of branded images and b-roll of Bright Haven Keepers.

Link to branded images and b-roll is attached to the brief in a text file.

Please message me any questions. Good luck to everyone in the project!

Target Market(s)

Male and Female working professionals between the ages of 30-60 years old.

Industry/Entity Type

Cleaning Service

Number of Pages Required

1 page

Font styles to use
Other font styles liked:
• Proxima Nova

Colors
0355a3
add136

Requirements
Must have
• Most of this is covered in the project description.
• Would like to have our logo split up so that the art of the maids remains the same but the "Brigade of Sweepers" text is to the right of the art. Looking for it to be a horizontal logo.
• Must use Proxima Nova font.
• Must use our branded images and videos. Feel free to create stills from the video.
Nice to have
• Nice to have, but not expected, is the b-roll edited to work with your design. We would like to see the designers vision of how the video would look with the website.
• Would be nice to have our logo given an updated look. Made horizontal as mentioned in the project description.
Should not have
• Should not feel busy. Should not use different color scheme than that of Tidy Corsairs. Should not have non-branded images of maids.

```html
<!DOCTYPE html>
<html lang="en">
<head>
<meta charset="utf-8">
<title>Brigade of Sweepers — Home</title>
<link href="https://fonts.googleapis.com/css2?family=Montserrat:wght@400;500;600;700;800&family=Open+Sans:wght@400;600;700&display=swap" rel="stylesheet">
<style>
:root{
  --blue:#0355a3;
  --blue-bright:#1f3fbf;
  --green:#add136;
  --green-text:#3fb43a;
  --page:#f1f8f7;
  --ink:#222;
  --muted:#777;
  --panel:#e8dfdf;
  --orange:#f08a4b;
  --flat:#5e92cc;
  --footer:#333436;
  --footer-text:#7d7d7d;
  --gold:#f3b81f;
}
*{box-sizing:border-box;margin:0;padding:0}
html,body{width:1200px;height:2667px;overflow:hidden}
body{position:relative;background:var(--page);font-family:"Open Sans",Arial,sans-serif;color:var(--ink)}
.abs{position:absolute}

/* top bar */
.topbar{left:0;top:0;width:1200px;height:32px;background:var(--blue);color:#fff;font-size:11px}
.topbar .contact{left:104px;top:9px;display:flex;gap:26px}
.topbar .contact span{display:flex;align-items:center;gap:7px}
.topbar .follow{right:108px;top:9px;display:flex;align-items:center;gap:9px;font-size:9px;letter-spacing:.5px}
.topbar .dot{width:9px;height:9px;border-radius:50%;background:#fff;opacity:.85}

/* header */
.header{left:0;top:32px;width:1200px;height:98px;background:var(--page)}
.logo{left:101px;top:22px;display:flex;align-items:center;gap:12px}
.logo .mark{width:52px;height:52px;border-radius:50%;background:var(--green)}
.logo .name{font-family:"Montserrat",sans-serif;font-weight:700;font-size:26px;color:var(--blue)}
.nav{left:462px;top:37px;display:flex;gap:2px;font-family:"Montserrat",sans-serif;font-size:11px;font-weight:700}
.nav a{color:#222;text-decoration:none;padding:8px 10px;white-space:nowrap}
.nav a.active{background:var(--blue);color:#fff}
.tollfree{left:1004px;top:30px;width:196px;height:40px;border-radius:20px 0 0 20px;background:var(--blue);border:3px solid #c9d9ec;border-right:none;color:#fff;display:flex;align-items:center;padding-left:12px;gap:6px;font-family:"Montserrat",sans-serif;white-space:nowrap}
.tollfree i{font-size:10px;font-style:italic}
.tollfree b{font-size:16px}
.tollfree small{font-size:9px;font-weight:600}

/* hero */
.hero{left:0;top:130px;width:1200px;height:546px;background:linear-gradient(120deg,#4a3a2e 0%,#8a7866 35%,#6f9a55 60%,#b9b2a4 100%)}
.hero h1{left:0;top:196px;width:1200px;text-align:center;color:#fff;font-family:"Montserrat",sans-serif;font-weight:700;font-size:44px;line-height:64px;text-shadow:0 2px 6px rgba(0,0,0,.45)}
.btn-hero{left:459px;top:352px;width:263px;height:50px;background:var(--blue);border:2px solid #fff;border-radius:4px;color:#fff;font-family:"Montserrat",sans-serif;font-weight:600;font-size:22px;display:flex;align-items:center;justify-content:center}

/* steps */
.step-circle{width:88px;height:88px;border-radius:50%;border:2px dashed #c7c7c7;background:#fff;display:flex;align-items:center;justify-content:center;font-family:"Montserrat",sans-serif;font-size:44px;font-weight:500;color:#9c9c9c;top:699px}
.step-label{top:726px;font-family:"Montserrat",sans-serif;font-size:23px;font-weight:400;white-space:nowrap}
.step-dash{top:746px;height:0;border-top:2px dashed #b8b8b8}

/* welcome */
.welcome h2{left:100px;top:822px;font-family:"Montserrat",sans-serif;font-weight:600;font-size:31px;color:#222}
.body-text{font-size:11.5px;line-height:23px;color:#666}
.feature{display:flex;gap:16px;align-items:flex-start;width:340px;font-size:12.5px;line-height:22px;color:#333}
.feature svg{flex:none}

/* form */
.form{left:812px;top:830px;width:290px;height:583px;background:var(--panel)}
.form-head{left:0;top:0;width:290px;height:42px;background:var(--blue);color:#fff;font-family:"Montserrat",sans-serif;font-size:19px;display:flex;align-items:center;justify-content:center}
.field{background:#fff;border:1px solid #cfcfcf;border-radius:2px;font-size:10px;color:#555;display:flex;align-items:center}
.form-label{width:290px;text-align:center;font-size:10.5px;font-weight:700;color:#333}
.note{font-size:8px;color:#888}
.stepper{left:36px;width:220px;height:36px;justify-content:space-between;padding:0 14px}
.toggle{top:141px;height:28px;color:#fff;font-size:10.5px;font-weight:700;display:flex;align-items:center;justify-content:center}
.btn-form{left:89px;top:530px;width:114px;height:34px;background:var(--blue);color:#fff;font-size:12px;font-weight:700;display:flex;align-items:center;justify-content:center}

/* content photos */
.frame-white{background:#fff}
.photo-workers{left:98px;top:1204px;width:652px;height:357px;background:linear-gradient(135deg,#d9d6cf,#3b3530 45%,#23324f 75%,#4f4944)}
.photo-team{left:809px;top:1470px;width:293px;height:240px;background:linear-gradient(180deg,#e9e9e9,#b8a08e 45%,#7cc94d 85%)}
.sub-head{font-family:"Montserrat",sans-serif;font-weight:500;font-size:15.5px;color:var(--blue);letter-spacing:.5px}

/* testimonials */
.clients-title{left:85px;top:1787px;width:345px;height:58px;background:#fff;font-family:"Montserrat",sans-serif;font-weight:700;font-size:25px;padding:14px 0 0 12px;color:#111}
.clients-title span{color:var(--blue-bright)}
.clients-title i{position:absolute;left:12px;bottom:8px;width:48px;height:4px;background:var(--gold)}
.avatar-box{width:118px;height:118px;background:#fff;display:flex;align-items:center;justify-content:center}
.avatar{width:104px;height:104px;border-radius:50%;border:4px solid var(--gold)}
.person{font-family:"Montserrat",sans-serif;font-weight:600;font-size:18px;color:#222}
.stars{display:flex;gap:3px}
.star{width:19px;height:19px;border-radius:50%;background:var(--gold)}

/* press */
.press-title{left:101px;top:2196px;font-family:"Montserrat",sans-serif;font-weight:700;font-size:29px;color:var(--blue-bright)}
.press{top:2276px;height:90px;display:flex;align-items:center;justify-content:center;font-family:"Montserrat",sans-serif;font-weight:700;font-size:24px;color:#333;white-space:nowrap}

/* footer */
.footer{left:0;top:2404px;width:1200px;height:263px;background:var(--footer);color:var(--footer-text)}
.footer .flogo{left:107px;top:52px;display:flex;align-items:center;gap:8px;font-family:"Montserrat",sans-serif;font-weight:700;font-size:15px;color:#8a8a8a;width:150px}
.footer .flogo i{width:30px;height:30px;border-radius:50%;background:#5a5a5a;flex:none}
.footer .about{left:270px;top:54px;width:365px;font-size:11.5px;line-height:23px}
.footer .links{left:754px;top:56px;font-size:11px;line-height:25px;color:#c9c9c9;list-style:none}
.footer .touch{left:923px;top:56px;font-size:11px;font-weight:700;color:#e5e5e5}
.footer .icons{left:923px;top:96px;display:flex;gap:26px}
.footer .icons i{width:12px;height:12px;border-radius:50%;background:#e5e5e5}
.footer .copy{left:0;top:220px;width:1200px;text-align:center;font-size:11px}
</style>
</head>
<body>

<!-- top bar -->
<div class="abs topbar">
  <div class="abs contact">
    <span><svg width="10" height="10" viewBox="0 0 10 10"><path d="M2 1l2 2-1 1.5c.6 1.2 1.3 1.9 2.5 2.5L7 6l2 2-1.5 1.5C4 9 1 6 .5 2.5z" fill="#fff"/></svg>(555) 010 2040</span>
    <span><svg width="12" height="9" viewBox="0 0 12 9"><rect x=".5" y=".5" width="11" height="8" fill="none" stroke="#fff"/><path d="M.5 .5L6 5l5.5-4.5" fill="none" stroke="#fff"/></svg>hello@brigadeofsweepers.example</span>
  </div>
  <div class="abs follow">FOLLOW US : <i class="dot"></i><i class="dot"></i><i class="dot"></i><i class="dot"></i><i class="dot"></i><i class="dot"></i></div>
</div>

<!-- header -->
<header class="abs header">
  <div class="abs logo"><i class="mark"></i><span class="name">Brigade of Sweepers</span></div>
  <nav class="abs nav">
    <a>HOME</a><a class="active">MAID SERVICES</a><a>GIFT CARDS</a><a>ABOUT US</a><a>CHARITY</a><a>CONTACT US</a>
  </nav>
  <div class="abs tollfree"><i>Toll Free</i><b>(855)</b><small>SWEEP NOW</small></div>
</header>

<!-- hero -->
<section class="abs hero" role="img" aria-label="Two maids in green uniforms cleaning a bright kitchen counter">
  <h1 class="abs">SUPER MAID SERVICE WITH ECO<br>FRIENDLY PRODUCTS</h1>
  <div class="abs btn-hero">Get Instant Price</div>
</section>

<!-- steps -->
<div class="abs step-circle" style="left:98px">1</div>
<div class="abs step-label" style="left:206px;color:var(--blue)">Cleaning</div>
<div class="abs step-dash" style="left:338px;width:88px"></div>
<div class="abs step-circle" style="left:441px">2</div>
<div class="abs step-label" style="left:549px;color:var(--green-text)">Pricing/Availability</div>
<div class="abs step-dash" style="left:830px;width:74px"></div>
<div class="abs step-circle" style="left:916px">3</div>
<div class="abs step-label" style="left:1026px;color:#777">Done!</div>

<!-- welcome -->
<section class="welcome">
  <h2 class="abs">Welcome to Brigade of Sweepers</h2>
  <p class="abs body-text" style="left:100px;top:884px;width:400px">Lorem ipsum dolor sit amet, consectetur adipiscing elit. Vestibulum at cursus neque. Integer tellus erat, sempeenim.</p>

  <div class="abs feature" style="left:103px;top:984px">
    <svg width="36" height="46" viewBox="0 0 36 46"><path d="M30 2L16 24" stroke="#222" stroke-width="3"/><path d="M12 22l10 6-6 14-12-6z" fill="#222"/><path d="M4 6l2 4 4 2-4 2-2 4-2-4-4-2 4-2z" fill="#222"/></svg>
    <span>Your friends and family will love how clean you home looks and smells!</span>
  </div>
  <div class="abs feature" style="left:441px;top:990px">
    <svg width="44" height="44" viewBox="0 0 44 44"><path d="M22 3l19 19-19 19L3 22V3z" fill="none" stroke="#222" stroke-width="4" transform="rotate(15 22 22)"/><circle cx="13" cy="13" r="3" fill="#222"/></svg>
    <span>Brigade of Sweepers is super flexible and affordable.</span>
  </div>
  <div class="abs feature" style="left:103px;top:1108px">
    <svg width="30" height="58" viewBox="0 0 30 58"><rect x="4" y="20" width="22" height="36" rx="4" fill="none" stroke="#222" stroke-width="3"/><rect x="9" y="8" width="12" height="12" fill="#222"/><path d="M21 10h8" stroke="#222" stroke-width="3"/></svg>
    <span>Let us handle the cleaning so you can have more free time.</span>
  </div>
  <div class="abs feature" style="left:448px;top:1110px">
    <svg width="36" height="48" viewBox="0 0 36 48"><circle cx="18" cy="17" r="15" fill="none" stroke="#222" stroke-width="3"/><circle cx="18" cy="17" r="8" fill="#222"/><path d="M9 30l-4 16 7-4 4 6 2-16M27 30l4 16-7-4-4 6" fill="#222"/></svg>
    <span>Backed by our unique 200% Guarantee. You have nothing to lose.</span>
  </div>
</section>

<!-- booking form -->
<aside class="abs form">
  <div class="abs form-head">Get a Price</div>
  <div class="abs field" style="left:36px;top:66px;width:220px;height:36px;padding-left:14px">Zip Code</div>
  <div class="abs form-label" style="top:120px">Cleaning Style</div>
  <div class="abs toggle" style="left:36px;width:110px;background:var(--flat)">Flat Rate</div>
  <div class="abs toggle" style="left:146px;width:110px;background:var(--orange)">Hourly</div>
  <div class="abs form-label" style="top:190px">Tell us about your home</div>
  <div class="abs field stepper" style="top:214px"><span>-</span><span>2 Bedrooms</span><span>+</span></div>
  <div class="abs note" style="left:36px;top:253px">(living room &amp; kitchen included)</div>
  <div class="abs field stepper" style="top:274px"><span>-</span><span>1 Bathroom</span><span>+</span></div>
  <div class="abs note" style="left:36px;top:314px">(round half baths up)</div>
  <div class="abs" style="left:36px;top:340px;font-size:10.5px;font-weight:700;color:#333">When would you like us to come?</div>
  <div class="abs field" style="left:36px;top:368px;width:107px;height:36px;padding-left:10px;justify-content:space-between;padding-right:8px">26-Dec-16
    <svg width="16" height="16" viewBox="0 0 16 16"><rect x="1" y="3" width="14" height="12" fill="none" stroke="#777"/><path d="M1 6h14M5 1v4M11 1v4" stroke="#777"/></svg></div>
  <div class="abs" style="left:36px;top:418px;font-size:10.5px;font-weight:700;color:#333">Any time between</div>
  <div class="abs field" style="left:36px;top:447px;width:50px;height:35px;justify-content:center">9 AM</div>
  <div class="abs" style="left:110px;top:458px;font-size:10px;color:#555">To</div>
  <div class="abs field" style="left:130px;top:447px;width:59px;height:35px;justify-content:center">8 PM</div>
  <svg class="abs" style="left:36px;top:500px" width="15" height="15" viewBox="0 0 15 15"><rect x=".5" y=".5" width="14" height="14" fill="#fff" stroke="#555"/><path d="M3 7.5l3 3 6-6" fill="none" stroke="#333" stroke-width="1.6"/></svg>
  <div class="abs" style="left:64px;top:501px;font-size:10.5px;color:var(--blue);font-weight:600">I'm flexible</div>
  <div class="abs btn-form">Get a Price</div>
</aside>

<!-- workers photo -->
<div class="abs frame-white" style="left:76px;top:1204px;width:30px;height:357px"></div>
<div class="abs photo-workers" role="img" aria-label="Two handymen in blue shirts fitting kitchen cabinets"></div>
<h3 class="abs sub-head" style="left:98px;top:1587px">CONSECTETUR ADIPISCING ELIT</h3>
<p class="abs body-text" style="left:98px;top:1621px;width:620px">Lorem ipsum dolor sit amet, consectetur adipiscing elit. Vestibulum at cursus neque. Integer tellus erat, semper ac faucibus sed, vulputate id enim. Ut placerat libero eget felis facilisis ullamcorper Vestibulum at cursus neque. Integer tellus erat, semper ac faucibus sed, vulputate id enim.</p>

<!-- team card -->
<div class="abs frame-white" style="left:777px;top:1524px;width:354px;height:316px"></div>
<div class="abs photo-team" role="img" aria-label="Two smiling maids in green uniforms"></div>
<h3 class="abs sub-head" style="left:814px;top:1732px;font-size:14.5px">CONSECTETUR A</h3>
<p class="abs body-text" style="left:814px;top:1763px;width:290px;font-size:11.5px">Etiam ultrices dui ut feugiat tristique. Aenean imperdiet diam condimentum purus tincidunt volutpat.</p>

<!-- testimonials -->
<div class="abs clients-title">WHAT OUR <span>CLIENT SAYS</span><i></i></div>

<div class="abs avatar-box" style="left:92px;top:1895px"><div class="avatar" role="img" aria-label="Client portrait" style="background:linear-gradient(#f7e6b0,#e8c070)"></div></div>
<div class="abs person" style="left:231px;top:1926px">AJ Deo</div>
<div class="abs stars" style="left:229px;top:1960px"><i class="star"></i><i class="star"></i><i class="star"></i><i class="star"></i><i class="star"></i></div>
<p class="abs body-text" style="left:100px;top:2032px;width:460px">Lorem ipsum dolor sit amet, consectetur adipiscing elit. Vestibulum at cursus neque. Integer tellus erat, semper ac faucibus sed, vulputate id enim. Ut placerat libero eget felis facilisis ullamcorper Vestibulum at cursus neque. Integer tellus erat, semper ac faucibus sed, vulputate id enim.</p>

<div class="abs avatar-box" style="left:626px;top:1895px"><div class="avatar" role="img" aria-label="Client portrait" style="background:linear-gradient(#e9d2c0,#b98a6c)"></div></div>
<div class="abs person" style="left:766px;top:1926px">Ajnli Deo</div>
<div class="abs stars" style="left:764px;top:1960px"><i class="star"></i><i class="star"></i><i class="star"></i><i class="star"></i><i class="star"></i></div>
<p class="abs body-text" style="left:642px;top:2023px;width:460px">Lorem ipsum dolor sit amet, consectetur adipiscing elit. Vestibulum at cursus neque. Integer tellus erat, semper ac faucibus sed, vulputate id enim. Ut placerat libero eget felis facilisis ullamcorper Vestibulum at cursus neque. Integer tellus erat, semper ac faucibus sed, vulputate id enim.</p>

<!-- press -->
<h2 class="abs press-title">WE HAVE BEEN FEATURED IN THESE PUBLICATIONS</h2>
<div class="abs press" style="left:101px;width:240px;justify-content:flex-start">Lakeside Courier</div>
<div class="abs press" style="left:390px;width:200px">Bayview Weekly</div>
<div class="abs press" style="left:617px;width:263px">greener living</div>
<div class="abs press" style="left:932px;width:163px">tidewater</div>

<!-- footer -->
<footer class="abs footer">
  <div class="abs flogo"><i></i>Brigade of Sweepers</div>
  <p class="abs about">Lorem ipsum dolor sit amet, consectetur adipiscing elit. Vestibulum at cursus neque. Integer tellus erat, semper ac faucibus sed, vulputate id enim. Ut placerat libero eget felis facilisis ullamcorper Vestibulum at cursus neque. Integer tellus erat, semper ac faucibus sed, vulputate id enim.</p>
  <ul class="abs links"><li>FAQ</li><li>Blog</li><li>Terms of Service</li><li>Privacy Policy</li><li>Jobs</li></ul>
  <div class="abs touch">Stay in touch</div>
  <div class="abs icons"><i></i><i></i><i></i><i></i></div>
  <div class="abs copy">Brigade of Sweepers All rights reserved. Copyright 2013-2014</div>
</footer>

</body>
</html>
```